Business Card Design Project

I would like to get a logo as well as business card and stationery.

i am in an event planner and coordination business. I need something sophisticated and elegant.

Business

```html
<!DOCTYPE html>
<html lang="en">
<head>
<meta charset="utf-8">
<title>Aster Bloom Events NYC — Business Card</title>
<link rel="stylesheet" href="https://fonts.googleapis.com/css2?family=Josefin+Sans:wght@300;400&family=Open+Sans:wght@400&display=swap">
<style>
  :root {
    --page-bg: #ffffff;
    --band-deep: #0c5f86;
    --band-mid: #14739f;
    --band-light: #1f8fc2;
    --stripe-grey: #a9abad;
    --card-top: #ffffff;
    --card-bottom: #dcdddf;
    --card-edge: #bfe3ef;
    --name-blue: #1a7aa0;
    --title-ink: #1e1e1e;
    --address-ink: #555555;
    --logo-ink: #ffffff;
    --mark-fill: #3db2e6;
  }
  html, body {
    margin: 0;
    padding: 0;
    width: 1200px;
    height: 800px;
    overflow: hidden;
    background: var(--page-bg);
  }
  .canvas {
    position: relative;
    width: 1200px;
    height: 800px;
  }
  .card {
    position: absolute;
    left: 179px;
    top: 164px;
    width: 814px;
    height: 499px;
    overflow: hidden;
    background: linear-gradient(180deg, var(--card-top) 40%, var(--card-bottom) 100%);
    border-bottom: 2px solid var(--card-edge);
  }
  .card-art {
    position: absolute;
    inset: 0;
    width: 100%;
    height: 100%;
  }
  .brand {
    position: absolute;
    left: 0;
    top: 112px;
    margin: 0;
    font-family: "Josefin Sans", sans-serif;
    font-weight: 300;
    font-size: 22px;
    letter-spacing: 0.5px;
    color: var(--logo-ink);
    white-space: nowrap;
  }
  .brand-mark {
    position: absolute;
    left: 122px;
    top: 36px;
    width: 86px;
    height: 86px;
    border-radius: 50%;
    background: var(--mark-fill);
  }
  .identity {
    position: absolute;
    left: 0;
    right: 0;
    top: 266px;
    display: flex;
    justify-content: center;
    align-items: center;
    font-family: "Josefin Sans", sans-serif;
    font-size: 36px;
    font-weight: 300;
    padding-right: 20px;
  }
  .identity-name {
    color: var(--name-blue);
    font-weight: 400;
    letter-spacing: 0.5px;
  }
  .identity-divider {
    display: inline-block;
    width: 1px;
    height: 30px;
    background: var(--title-ink);
    margin: 0 6px 0 16px;
  }
  .identity-role {
    color: var(--title-ink);
    font-weight: 400;
  }
  .address {
    position: absolute;
    left: 0;
    right: 0;
    top: 426px;
    margin: 0;
    text-align: center;
    font-family: "Open Sans", sans-serif;
    font-style: normal;
    font-size: 20px;
    line-height: 29px;
    color: var(--address-ink);
  }
</style>
</head>
<body>
<main class="canvas">
  <section class="card">
    <svg class="card-art" viewBox="0 0 814 499" preserveAspectRatio="none" aria-hidden="true">
      <defs>
        <linearGradient id="band-fill" x1="0" y1="1" x2="0.6" y2="0">
          <stop offset="0" stop-color="var(--band-light)"/>
          <stop offset="0.55" stop-color="var(--band-mid)"/>
          <stop offset="1" stop-color="var(--band-deep)"/>
        </linearGradient>
        <linearGradient id="swoosh-fill" x1="0" y1="0" x2="1" y2="1">
          <stop offset="0" stop-color="#ffffff" stop-opacity="0"/>
          <stop offset="1" stop-color="#ffffff" stop-opacity="0.7"/>
        </linearGradient>
      </defs>
      <path class="soft-swoosh" d="M120 499 C 380 420, 640 330, 814 290 L 814 499 Z" fill="url(#swoosh-fill)"/>
      <path class="band-stripe" d="M0 194 L0 202 C 260 200, 560 160, 814 120 L 814 110 C 560 150, 260 192, 0 194 Z" fill="var(--stripe-grey)"/>
      <path class="top-band" d="M0 0 L814 0 L814 113 C 560 152, 260 192, 0 194 Z" fill="url(#band-fill)"/>
      <path class="band-sheen" d="M60 0 C 120 60, 220 110, 360 150 L 0 194 L 0 0 Z" fill="#ffffff" fill-opacity="0.06"/>
    </svg>

    <span class="brand-mark" aria-hidden="true"></span>
    <p class="brand">Aster Bloom Events NYC</p>

    <h1 class="identity">
      <span class="identity-name">Rafiul Karim</span>
      <span class="identity-divider" aria-hidden="true"></span>
      <span class="identity-role">Co Founder</span>
    </h1>

    <address class="address">
      512, Cobalt Crest Tower, Harbour Point Towers<br>
      Dubai, U.A.E
    </address>
  </section>
</main>
</body>
</html>
```